Orbit 582 - Kindle Book Cover

I am looking for a Kindle book cover for my book about "Orbit 582".
The Book is Titled:
Orbit 582 Ascended
Shaping Tomorrow: Paths To Unlocking Hidden Currents
Author is Dorian Welby
Here is a book description that may help you understand more about it:
Inspired by the genius of Bertram Ollinger, this comprehensive guide delves into the ancient wisdom and cutting-edge science behind the 582 method, a powerful tool for manifesting your desires. Whether you're seeking personal growth, financial success, or spiritual enlightenment, this book provides advanced techniques and methods to transform your dreams into reality.
Any questions please ask.
Thanks
Gavin

```html
<!DOCTYPE html>
<html lang="en">
<head>
<meta charset="UTF-8">
<title>Orbit 582 Ascended — Dorian Welby</title>
<link href="https://fonts.googleapis.com/css2?family=Archivo+Black&family=Poppins:wght@300;700;800&family=Sacramento&display=swap" rel="stylesheet">
<style>
  :root {
    --paper: #ffffff;
    --navy: #1a5192;
    --coral: #e2807a;
    --blush: #f9b9a9;
  }
  html, body {
    margin: 0;
    padding: 0;
    overflow: hidden;
    background: var(--paper);
  }
  .cover {
    position: relative;
    width: 750px;
    height: 1200px;
    background: var(--paper);
    overflow: hidden;
  }
  .series-word {
    position: absolute;
    left: 56px;
    top: 42px;
    margin: 0;
    font-family: "Poppins", sans-serif;
    font-weight: 700;
    font-size: 62px;
    line-height: 1;
    color: var(--coral);
  }
  .series-digit {
    position: absolute;
    left: 46px;
    width: 190px;
    font-family: "Archivo Black", sans-serif;
    font-size: 320px;
    line-height: 1;
    color: var(--navy);
    text-align: center;
    transform: skewX(-6deg);
  }
  .digit-one { top: 120px; }
  .digit-two { top: 390px; }
  .digit-three { top: 660px; }
  .bulb-art {
    position: absolute;
    left: 296px;
    top: 132px;
    width: 388px;
    height: 740px;
    border-radius: 194px 194px 90px 90px / 230px 230px 60px 60px;
    background: linear-gradient(180deg, #fdeeea 0%, var(--blush) 60%, var(--coral) 100%);
  }
  .edition-word {
    position: absolute;
    left: 90px;
    top: 790px;
    width: 620px;
    height: 210px;
    overflow: visible;
  }
  .edition-word text {
    font-family: "Sacramento", cursive;
    font-size: 170px;
    fill: var(--coral);
  }
  .subtitle {
    position: absolute;
    left: 253px;
    top: 1006px;
    margin: 0;
    font-family: "Poppins", sans-serif;
    font-weight: 300;
    font-size: 21px;
    line-height: 1.45;
    color: var(--coral);
  }
  .author {
    position: absolute;
    left: 56px;
    top: 1098px;
    margin: 0;
    font-family: "Poppins", sans-serif;
    font-weight: 800;
    font-size: 64px;
    line-height: 1;
    letter-spacing: 0.2em;
    color: var(--navy);
    white-space: nowrap;
  }
</style>
</head>
<body>
  <main class="cover">
    <h1 class="series-word">Orbit</h1>
    <div class="series-digit digit-one">5</div>
    <div class="series-digit digit-two">8</div>
    <div class="series-digit digit-three">2</div>
    <div class="bulb-art" role="img" aria-label="Illustration of a light bulb with a hand making a victory sign inside it"></div>
    <svg class="edition-word" viewBox="0 0 620 210" aria-label="Ascended">
      <text x="6" y="168" textLength="600" lengthAdjust="spacingAndGlyphs">Ascended</text>
    </svg>
    <p class="subtitle">Shaping Tomorrow:<br>Paths To Unlocking Hidden Currents</p>
    <p class="author">DORIAN WELBY</p>
  </main>
</body>
</html>
```